Retail Package for Ammunition Company

We are looking for a packaging design for a retail boxed ammunition. The "look". Attached will be the logo to be used. The logo is attached and a can be manipulated on the box. Box to represent strength and accuracy. Will need to provide .psd files to allow in house personnel to add/remove text to other calibers and warnings. Wow me with your designs!

Browse Other Brands: http://www.brightfalconstore.com/brands

The packaging needs to include:
Logo- provided and the following text:

FRONT 1. 9mm 115gr FMJ

BACK 2. WARNING: To avoid serious injury: (1) use only ammunition in good condition; use only in modern firearms in good condition marked for .22 Long Rifle (LR) cartridges; (2) always be sure barrel is free of any obstructions; the barrel should be checked in case of light recoil, or an unusually loud or weak sound heard during firing; (3) wear eye and ear protection; (4) if gun fails to fire, avoid exposure to breech when unloading and point muzzle in a safe direction. Keep firearm pointed in safe direction at all times; (5) discharge may occur if rim is struck; handle with caution, do not drop. (6) Do not shoot at hard surfaces or water to prevent ricochet; (7) Bullet is capable of traveling extreme distances. Know your backstop; (8) Store in cool dry place

3. LEAD WARNING: Discharging firearms in poorly ventilated areas, cleaning firearms, or handling ammunition may result in exposure to lead and other substances known to cause birth defects, reproductive harm, and other serious physical injury. Have adequate ventilation at all times. Wash hands thoroughly after exposure.

Dimensions ; (LxWxH): 5.25" x 2.625" x 1.125"

Target Market(s)

Ammunition Industry

```html
<!DOCTYPE html>
<html lang="en">
<head>
<meta charset="utf-8">
<title>Stone Harrier Arms – 9MM 115GR FMJ Retail Box</title>
<link rel="stylesheet" href="https://fonts.googleapis.com/css2?family=Bebas+Neue&family=Open+Sans:wght@700;800&family=Tinos:wght@400;700&display=swap">
<style>
  :root {
    --yellow: #f8ea00;
    --band-yellow: #e2e626;
    --maroon: #8e1414;
    --navy: #1b1f78;
    --royal: #1238e0;
    --sky: #38bff4;
    --blue: #1f8ae8;
    --violet: #6d6df6;
    --lilac: #9a98f4;
    --dusk: #3b3c76;
    --paper: #f4f4f4;
    --white: #ffffff;
  }
  * { box-sizing: border-box; margin: 0; padding: 0; }
  html, body { width: 1200px; height: 1173px; overflow: hidden; }
  body { background: var(--paper); font-family: "Open Sans", sans-serif; }
  .canvas { position: relative; width: 1200px; height: 1173px; overflow: hidden;
    background: linear-gradient(160deg, #ffffff 0%, #f3f3f3 60%, #e6e6e6 100%); }

  .piece { position: absolute; overflow: hidden; container-type: size; }
  .shadowed { box-shadow: 3px 4px 6px rgba(0,0,0,.25); }

  /* brand lockup */
  .brand { display: flex; align-items: center; gap: .35em; }
  .brand-mark { width: 1.6em; height: 1.6em; background: var(--maroon); flex: none; }
  .brand-name { font-family: "Open Sans", sans-serif; font-weight: 800; color: var(--maroon);
    line-height: 1.02; letter-spacing: .02em; text-transform: uppercase; }

  /* hazard flaps */
  .hazard { background: linear-gradient(135deg, var(--yellow) 0%, #c9741a 50%, var(--yellow) 100%); }

  /* ---------- front panel ---------- */
  .front { background: linear-gradient(100deg, var(--violet) 0%, var(--lilac) 45%, var(--dusk) 100%); }
  .front .lower { position: absolute; left: 0; right: 0; top: 42%; bottom: 0;
    background: linear-gradient(165deg, #6f7cf6 0%, var(--sky) 35%, var(--blue) 100%); }
  .front .brand { position: absolute; left: 8%; top: 8%; font-size: 8.5cqh; }
  .front .checker { position: absolute; left: 75%; top: 6%; width: 21%; height: 33%; background: var(--yellow); opacity: .95; }
  .bar { position: absolute; }
  .front .bar-yellow { left: 65%; right: 0; top: 25%; height: 3.6%; background: var(--yellow); }
  .front .bar-pale { left: 0; right: 0; top: 32%; height: 3.4%; background: #8ec9fb; }
  .front .bar-royal { left: 27%; right: 0; top: 39%; height: 4%; background: var(--royal); }
  .front .bar-cyan { left: 50%; right: 0; top: 46.5%; height: 3.8%; background: #4fc9f4; }
  .front .band { position: absolute; left: 0; right: 0; top: 55%; height: 21%;
    background: linear-gradient(100deg, #e9e640, var(--band-yellow)); }
  .front .target { position: absolute; left: 7%; top: 45%; width: 17%; height: 39%; border-radius: 50%;
    background: radial-gradient(circle, #111 0 18%, #d8dc50 19% 100%); border: 1px solid #222; }
  .title { font-family: "Bebas Neue", sans-serif; color: var(--band-yellow); white-space: nowrap;
    -webkit-text-stroke: 1.2px var(--navy); line-height: 1; letter-spacing: .01em; }
  .front .title { position: absolute; left: 27%; top: 54%; font-size: 24cqh;
    text-shadow: .05em .05em 0 var(--navy); }
  .front .sub { position: absolute; left: 27%; right: 6%; top: 80%; text-align: center;
    font-weight: 700; font-size: 5cqh; color: var(--yellow); white-space: nowrap; }

  /* ---------- side bands ---------- */
  .side { background: linear-gradient(100deg, var(--band-yellow), #d6e62a); }
  .side .edge-top, .side .edge-bottom { position: absolute; left: 0; right: 0; }
  .side .brand { position: absolute; left: 7%; top: 50%; transform: translateY(-50%); font-size: 16cqh; }
  .side .title { position: absolute; left: 33%; right: 4%; top: 50%; transform: translateY(-50%);
    text-align: center; font-size: 58cqh; -webkit-text-stroke: 1px var(--navy);
    text-shadow: .04em .04em 0 var(--navy); }

  /* ---------- back panel ---------- */
  .back { background: linear-gradient(125deg, #7a7af7 0%, #6f8cf6 22%, var(--sky) 40%, var(--blue) 62%, #5a6bf5 100%); }

  /* warning block, rotated to read bottom-up */
  .warning { position: absolute; background: var(--navy); border: 3px solid var(--yellow); container-type: size; }
  .warning-turn { position: absolute; left: 50%; top: 50%; width: 100cqh; height: 100cqw;
    transform: translate(-50%, -50%) rotate(-90deg); container-type: size; padding: 6cqw 7cqw; color: var(--white);
    font-family: "Tinos", serif; }
  .warning-head { display: flex; align-items: center; gap: 4cqw; }
  .warning-head .brand-mark { width: 8cqw; height: 8cqw; background: var(--yellow); }
  .warning-title { font-family: "Bebas Neue", sans-serif; color: var(--yellow); font-size: 13cqw; line-height: 1; letter-spacing: .04em; }
  .warning-sub { font-size: 6cqw; margin-top: 3cqw; text-transform: uppercase; }
  .warning p { font-size: 3.2cqw; line-height: 1.15; text-transform: uppercase; margin-top: 3cqw; }

  /* caliber info strip */
  .info { position: absolute; container-type: size; }
  .info .checker { position: absolute; left: 6%; top: 4%; width: 17%; height: 92%; background: var(--yellow); }
  .vtext { writing-mode: vertical-rl; transform: rotate(180deg); }
  .info .cal { position: absolute; left: 29%; top: 50%; translate: 0 -50%; font-family: "Bebas Neue", sans-serif;
    font-size: 44cqh; color: var(--royal); -webkit-text-stroke: 1px var(--navy); line-height: 1;
    text-shadow: -.04em .04em 0 var(--navy); }
  .info .bullet { position: absolute; left: 42%; top: 2%; width: 37%; height: 96%;
    background: #2f8cf0; border-radius: 45% 8% 8% 45% / 50% 10% 10% 50%;
    display: flex; align-items: center; justify-content: center; gap: 3cqh; }
  .info .bullet span { font-size: 23cqh; color: var(--yellow); line-height: 1.05; font-family: "Open Sans", sans-serif; font-weight: 700; letter-spacing: .04em; }
  .info .bullet .rule { width: 3cqh; height: 55%; background: var(--royal); }
  .info .burst { position: absolute; left: 83%; top: 50%; width: 56cqh; height: 56cqh; translate: 0 -50%;
    border-radius: 50%; background: radial-gradient(circle, #4e7cf0 0 25%, #dde7ff 70%); }

  /* end panels */
  .end { background: var(--yellow); }
  .end-front .brand { position: absolute; left: 50%; top: 50%; font-size: 16cqw;
    transform: translate(-50%, -50%) rotate(-90deg); white-space: nowrap; }
  .end-logo .brand { position: absolute; left: 50%; top: 50%; transform: translate(-50%, -50%); font-size: 15cqh; white-space: nowrap; }
</style>
</head>
<body>
<main class="canvas">

  <!-- dieline: top flap + front -->
  <div class="piece hazard" style="left:57px;top:40px;width:100px;height:231px" role="img" aria-label="Diagonal yellow and maroon hazard stripes"></div>

  <section class="piece front" style="left:157px;top:40px;width:464px;height:256px">
    <div class="lower"></div>
    <div class="brand"><span class="brand-mark"></span><span class="brand-name">Stone Harrier<br>Arms</span></div>
    <div class="bar bar-pale"></div>
    <div class="bar bar-royal"></div>
    <div class="bar bar-cyan"></div>
    <div class="checker" role="img" aria-label="Yellow diamond checker pattern"></div>
    <div class="bar bar-yellow"></div>
    <div class="band"></div>
    <div class="target" role="img" aria-label="Shooting target with bullet"></div>
    <div class="title">9MM 115GR FMJ</div>
    <div class="sub">9 millimeters // 115 grain // full metal jacket</div>
  </section>

  <section class="piece end end-front" style="left:622px;top:40px;width:100px;height:231px">
    <div class="brand"><span class="brand-mark"></span><span class="brand-name">Stone Harrier<br>Arms</span></div>
  </section>

  <section class="piece side" style="left:157px;top:296px;width:464px;height:55px">
    <div class="brand"><span class="brand-mark"></span></div>
    <div class="title">9MM 115GR FMJ</div>
  </section>

  <section class="piece back" style="left:157px;top:351px;width:464px;height:353px">
    <div class="warning" style="left:29px;top:34px;width:405px;height:209px">
      <div class="warning-turn">
        <div class="warning-head"><span class="brand-mark"></span><span class="warning-title">Warning</span></div>
        <div class="warning-sub">To avoid serious injury:</div>
        <p>(1) Use only ammunition in good condition; use only in modern firearms in good condition marked for .22 Long Rifle (LR) cartridges; (2) always be sure barrel is free of any obstructions; the barrel should be checked in case of light recoil, or an unusually loud or weak sound heard during firing; (3) wear eye and ear protection; (4) if gun fails to fire, avoid exposure to breech when unloading and point muzzle in a safe direction. Keep firearm pointed in safe direction at all times; (5) discharge may occur if rim is struck; handle with caution, do not drop. (6) Do not shoot at hard surfaces or water to prevent ricochet; (7) bullet is capable of traveling extreme distances. Know your backstop; (8) store in cool dry place</p>
        <p>Lead warning: discharging firearms in poorly ventilated areas, cleaning firearms, or handling ammunition may result in exposure to lead and other substances known to cause birth defects, reproductive harm, and other serious physical injury. Have adequate ventilation at all times. Wash hands thoroughly after exposure.</p>
      </div>
    </div>
    <div class="info" style="left:0;top:262px;width:464px;height:86px">
      <div class="checker" role="img" aria-label="Yellow diamond checker pattern"></div>
      <div class="cal vtext">9MM</div>
      <div class="bullet"><span class="vtext">115<br>GRAIN</span><span class="rule"></span><span class="vtext">FULL<br>METAL<br>JACKET</span></div>
      <div class="burst" role="img" aria-label="Radiating sunburst emblem"></div>
    </div>
  </section>

  <!-- separate panels -->
  <section class="piece back shadowed" style="left:763px;top:67px;width:386px;height:195px">
    <div class="warning" style="left:24px;top:10px;width:337px;height:176px">
      <div class="warning-turn">
        <div class="warning-head"><span class="brand-mark"></span><span class="warning-title">Warning</span></div>
        <div class="warning-sub">To avoid serious injury:</div>
        <p>(1) Use only ammunition in good condition; use only in modern firearms in good condition marked for .22 Long Rifle (LR) cartridges; (2) always be sure barrel is free of any obstructions; the barrel should be checked in case of light recoil, or an unusually loud or weak sound heard during firing; (3) wear eye and ear protection; (4) if gun fails to fire, avoid exposure to breech when unloading and point muzzle in a safe direction. Keep firearm pointed in safe direction at all times; (5) discharge may occur if rim is struck; handle with caution, do not drop. (6) Do not shoot at hard surfaces or water to prevent ricochet; (7) bullet is capable of traveling extreme distances. Know your backstop; (8) store in cool dry place</p>
        <p>Lead warning: discharging firearms in poorly ventilated areas, cleaning firearms, or handling ammunition may result in exposure to lead and other substances known to cause birth defects, reproductive harm, and other serious physical injury. Have adequate ventilation at all times. Wash hands thoroughly after exposure.</p>
      </div>
    </div>
  </section>

  <section class="piece side shadowed" style="left:716px;top:333px;width:419px;height:88px;background:linear-gradient(180deg,var(--sky) 0 20%,var(--band-yellow) 20% 78%,var(--violet) 78%)">
    <div class="brand"><span class="brand-mark"></span></div>
    <div class="title" style="font-size:44cqh">9MM 115GR FMJ</div>
  </section>

  <section class="piece back shadowed" style="left:711px;top:445px;width:420px;height:90px">
    <div class="info" style="left:0;top:0;width:420px;height:90px">
      <div class="checker" role="img" aria-label="Yellow diamond checker pattern"></div>
      <div class="cal vtext">9MM</div>
      <div class="bullet"><span class="vtext">115<br>GRAIN</span><span class="rule"></span><span class="vtext">FULL<br>METAL<br>JACKET</span></div>
      <div class="burst" role="img" aria-label="Radiating sunburst emblem"></div>
    </div>
  </section>

  <section class="piece end end-logo shadowed" style="left:679px;top:560px;width:233px;height:100px">
    <div class="brand"><span class="brand-mark"></span><span class="brand-name">Stone Harrier<br>Arms</span></div>
  </section>

  <div class="piece hazard shadowed" style="left:941px;top:562px;width:233px;height:100px" role="img" aria-label="Diagonal yellow and maroon hazard stripes"></div>

  <section class="piece front shadowed" style="left:29px;top:798px;width:614px;height:309px">
    <div class="lower"></div>
    <div class="brand"><span class="brand-mark"></span><span class="brand-name">Stone Harrier<br>Arms</span></div>
    <div class="bar bar-pale"></div>
    <div class="bar bar-royal"></div>
    <div class="bar bar-cyan"></div>
    <div class="checker" role="img" aria-label="Yellow diamond checker pattern"></div>
    <div class="bar bar-yellow"></div>
    <div class="band"></div>
    <div class="target" role="img" aria-label="Shooting target with bullet"></div>
    <div class="title">9MM 115GR FMJ</div>
    <div class="sub">9 millimeters // 115 grain // full metal jacket</div>
  </section>

</main>
</body>
</html>
```